Newsletter/Flyer/Advertisement - ("Call for Papers") Design Project

We will be arranging a conference on electronics integration technology in Saarela, Finland in September 2014 and we would need catchy looking information leaflet to advertise it. We call this a “call for papers” and it is distributed to all potential attendants of the conference. I have attached the plain text part as a MS Word document “1st Call for Papers.docx”. The title format, font etc. can be changed and modified but the 1/2/1 column layout should remain the same and the text should not extend to third page.
There are 5 logos that must be included; the event logo QRVN2014 should be on the front page but the remaining 4 logos (Birchmoor University, OKUW, LDZB, and uTROF) should be placed in the bottom footer of both pages. I have attached the call for papers from the previous QRVN conference (in 2012) as a reference of how it has looked before. However, I would like to make it visually little bit more like the GWYH call for papers, which is also attached. If you can find a little "flavor" perhaps from the theme of the conference (electronics) and/or something local (Saarela) to make it stand out next to the old QRVN one. I think the theme of electronics is quite universal but I will also attach some photos of Saarela.
Please do not hesitate to ask for clarifications!
Updates

Target Market(s)

Technical people and academics around the world

Industry/Entity Type

Electronics

Requirements
Must have
• Texh included in the "1st Call for Papers.docx". 5 logos: the QRVN2014 event logo somewhere up in the front; Birchmoor University, OKUW, LDZB, and uTROF logos down in the bottom footer (in this particular order).
Nice to have
• Some local "flavor" from Saarela and the theme of the conference (microelectronics) present in the appearance.

```html
<!DOCTYPE html>
<html lang="en">
<head>
<meta charset="utf-8">
<title>QRVN 2014 – First Call for Papers</title>
<link rel="stylesheet" href="https://fonts.googleapis.com/css2?family=Russo+One&family=Arimo:ital,wght@0,400;0,700;1,400;1,700&display=swap">
<style>
:root{
  --blue:#1a8fd6;
  --blue-deep:#0b6fb5;
  --blue-dark:#0a4f86;
  --tab:#d9dadb;
  --ink:#222;
  --white:#fff;
  --bg:#e6e7e8;
  --night-1:#0c1f3f;
  --night-2:#3a5784;
  --night-3:#c98a3e;
}
*{box-sizing:border-box;margin:0;padding:0}
html,body{width:1200px;height:801px;overflow:hidden}
body{background:var(--bg);font-family:"Arimo",Arial,sans-serif;color:var(--ink);position:relative}
.page{position:absolute;top:26px;width:550px;height:748px;background:var(--white);box-shadow:0 3px 12px rgba(0,0,0,.25);overflow:hidden}
.page--front{left:40px}
.page--back{left:610px}
p{font-size:8px;line-height:1.36;text-align:justify}

/* front header */
.hero-photo{position:absolute;left:0;top:0;width:550px;height:152px;background:linear-gradient(180deg,var(--night-1) 0%,var(--night-2) 55%,var(--night-3) 100%)}
.event-mark{position:absolute;left:14px;top:0;width:128px;height:104px;background:var(--white);display:flex;flex-direction:column;align-items:center;justify-content:center;gap:6px;padding:0 8px;text-align:center;color:var(--blue-deep);font-weight:700}
.event-mark__name{font-size:18px}
.event-mark__sub{font-size:6.5px;line-height:1.25}
.title-band{position:absolute;left:0;top:152px;width:550px;height:64px;background:linear-gradient(180deg,var(--blue) 0%,var(--blue-deep) 100%);color:var(--white);text-align:center;padding-top:7px}
.title-band h1{font-family:"Russo One",sans-serif;font-weight:400;font-size:27px;letter-spacing:.5px}
.title-band h2{font-family:"Russo One",sans-serif;font-weight:400;font-size:12px;margin-top:3px;letter-spacing:.3px}
.event-date{position:absolute;left:0;top:224px;width:550px;text-align:center;color:var(--blue-deep);font-weight:700;font-size:15px}
.event-url{position:absolute;left:0;top:243px;width:550px;text-align:center;color:var(--blue-deep);font-size:8px}
.intro{position:absolute;left:22px;top:260px;width:506px;font-style:italic}

.column{position:absolute;display:flex;flex-direction:column;gap:8px}
.column--left{left:22px;top:325px;width:250px}
.column--right{left:280px;top:316px;width:250px}
.info-box{background:var(--blue);color:var(--white);padding:6px 8px 8px;box-shadow:2px 2px 4px rgba(0,0,0,.3)}
.info-box p{color:var(--white)}
.tab-heading{display:inline-block;background:var(--tab);color:var(--blue-deep);font-weight:700;font-size:12px;padding:3px 26px 3px 6px;margin:0 0 5px -8px}
.track{color:var(--white);font-weight:700;font-size:8.6px;margin:6px 0 2px}
.track:first-child{margin-top:0}

.partner-footer{position:absolute;left:0;bottom:0;width:550px;height:82px;display:flex;justify-content:space-around;align-items:center;padding:0 14px}
.partner{display:flex;align-items:center;gap:6px;color:var(--blue-dark);font-weight:700;font-size:16px}
.partner__dot{width:30px;height:30px;border-radius:50%;background:var(--blue-dark)}
.partner__sq{width:26px;height:26px;background:var(--blue-dark)}
.partner--small{font-size:11px}

/* back */
.print-box{position:absolute;left:22px;top:0;width:258px;height:158px;padding-top:10px}
.section-tab{position:absolute;background:var(--tab);color:var(--blue-deep);font-weight:700;font-size:12.5px;padding:4px 14px 4px 10px;box-shadow:1px 1px 3px rgba(0,0,0,.2)}
.back-text{position:absolute}
.back-text p + p{margin-top:3px}
.dates-list{list-style:none;font-size:8px;line-height:2.1}
.dates-list li::before{content:"";display:inline-block;width:5px;height:5px;border-radius:50%;background:var(--blue);margin-right:4px}
.welcome-band{position:absolute;left:0;top:430px;width:550px;height:70px;background:var(--blue);color:var(--white);font-style:italic;font-weight:700;font-size:14px;text-align:center;padding-top:12px;line-height:1.45}
.chairs{position:absolute;left:0;top:518px;width:550px;display:flex;justify-content:space-around;text-align:center}
.chair__name{color:var(--blue-deep);font-style:italic;font-weight:700;font-size:8.5px}
.chair__role{font-size:9px;margin-top:6px}
.city-photo{position:absolute;left:0;top:568px;width:550px;height:180px;background:linear-gradient(180deg,#fff 0%,#cfcfcf 35%,#8a8a8a 65%,#e8e8e8 100%)}
</style>
</head>
<body>

<section class="page page--front" aria-label="Front page">
  <div class="hero-photo" role="img" aria-label="Night view of a harbour with lit buildings and a tall ship"></div>
  <div class="event-mark">
    <span class="event-mark__name">QRVN2014</span>
    <span class="event-mark__sub">Electronics Module-Assembly Technology Conference</span>
  </div>
  <header class="title-band">
    <h1>FIRST CALL FOR PAPERS</h1>
    <h2>ELECTRONIC MODULE-ASSEMBLY TECHNOLOGY (QRVN) CONFERENCE</h2>
  </header>
  <div class="event-date">October 6 – 9, 2014, Saarela, Finland</div>
  <div class="event-url">www.qrvn2014.eu (http://198.51.100.42)</div>
  <p class="intro">It is our pleasure to announce that the 5th QRVN Conference, the premier European event in the field of microelectronics packaging and integration, will be held 6th – 9th of October, 2014, at Harbourline Hall in Saarela, Finland. This international event brings together both academics as well as the industry leaders to discuss and debate the state-of-the-art and the future trends in packaging and integration technologies. QRVN provides a perfect opportunity to hear the latest news and developments in the field. So mark the dates down on your calendar now!</p>

  <div class="column column--left">
    <div class="info-box">
      <span class="tab-heading">Background</span>
      <p>The QRVN conference is organized by OKUW-LDZB in association with uTROF-Europe. The 2014 event continues the line of prestigious events since the birth of the conference in Lindenfeld, Germany in 2006, and followed by Marlow Bay, Ostheim, and Veldmere every even year. QRVN is truly an international event as people from 26 countries attended the 4th QRVN conference in Veldmere.</p>
    </div>
    <div class="info-box">
      <span class="tab-heading">Call for Papers</span>
      <p>QRVN 2014 seeks original papers describing research in all areas of electronic packaging. You are invited to submit abstracts that provide non-commercial information on new developments and knowledge in the areas including, but not limited to examples given for each technical track:</p>
      <div class="track">3D integration and embedding technologies:</div>
      <p>Challenges and solutions in 3D integration, embedded, and wafer level packaging, micro-bonding, TSVs, TEVs, advanced substrates and interposers, etc.</p>
      <div class="track">Advanced and Emerging Technologies:</div>
      <p>allotropes of carbon (CNTs, graphene, DLC, etc.), emerging packaging concepts and technologies, microfluidics, bio-electronics, flexible and stretchable electronics, etc.</p>
    </div>
  </div>

  <div class="column column--right">
    <div class="info-box">
      <div class="track">Assembly and Manufacturing Technology:</div>
      <p>novel assembly technologies, manufacturing aspects to novel packaging, wafer level processing, etc.</p>
      <div class="track">Materials for Interconnect and Packaging:</div>
      <p>new materials and processing – e.g. phase change, piezo-electric, self-organizing, and memory materials, dielectric materials, advanced interconnection metallurgies, etc.</p>
      <div class="track">MEMS/NEMS packaging:</div>
      <p>challenges and solutions in processing, integration, and packaging, new packaging approaches, bonding technologies: wafer bonding, micro-bonding, etc.</p>
      <div class="track">Modeling in Electronics:</div>
      <p>Thermal, mechanical, and electrical modeling and experimental verifications, signal and power integrity, etc.</p>
      <div class="track">Optoelectronic Packaging:</div>
      <p>Fiber optical interconnects, optical sensors, LEDs and other photonic devices, optical chip-scale and heterogeneous integration, lasers, etc.</p>
      <div class="track">Power Electronic Packaging:</div>
      <p>high performance packaging (low RDS(on); high temperature), Si power diode and thyristor devices, wide bandgap power semiconductor devices (e.g. SiC, GaN, GaAs), novel cooling solutions, etc.</p>
    </div>
  </div>

  <footer class="partner-footer">
    <div class="partner"><span class="partner__dot"></span>OKUW</div>
    <div class="partner">LDZB</div>
    <div class="partner partner--small"><span class="partner__sq"></span>Birchmoor University</div>
    <div class="partner"><span class="partner__dot"></span>uTROF</div>
  </footer>
</section>

<section class="page page--back" aria-label="Back page">
  <div class="info-box print-box">
    <div class="track">Printable electronics:</div>
    <p>printed/jetted (transparent) conductors, touch sensors, screens and displays (e.g. OLED), paper electronics, 3D printing, PV, etc.</p>
    <div class="track" style="margin-top:12px">Reliability:</div>
    <p>challenges at different levels of investigations (system, board, package and joint), characterization and test methods, interconnection reliability; characterization, and next generation/novel packaging reliability.</p>
  </div>

  <div class="section-tab" style="left:10px;top:170px">Abstract Submission</div>
  <div class="back-text" style="left:24px;top:205px;width:250px">
    <p>You are invited to submit a 300-500 word abstract that describes the scope, content and key points of your proposed paper. Abstracts must include results and graphics. The official language of all presentations is English. Please visit www.qrvn2014.eu to find more information and to upload your abstract. Submission of abstracts will be opened 1.1.2014 and the abstracts are due 28.2.2014. All abstracts must be submitted electronically at the conference web site.</p>
    <p>All submitted abstracts will be reviewed by the committee to ensure a high-quality conference. Authors will be notified of paper acceptance with instructions for publication by 18.4.2014.</p>
    <p>If you have any questions, please contact: Lauren Vadeboncoeur, Program Chair of the 5th QRVN, via email (firstname.lastname@mail-example.org).</p>
  </div>

  <div class="section-tab" style="left:278px;top:10px">Publication of Papers</div>
  <div class="back-text" style="left:286px;top:38px;width:242px">
    <p>All oral and poster presentation papers will be included in the conference proceedings and made available at the OKUW Archive Digital Library (archive.okuw.org).</p>
    <p style="margin-top:7px">In order to be included in OKUW Archive the paper must be original and not previously published, and avoid inclusion of commercial content.</p>
  </div>

  <div class="section-tab" style="left:278px;top:124px">Best Paper Awards</div>
  <div class="back-text" style="left:286px;top:152px;width:242px">
    <p>QRVN will select the best paper presentation. The author(s) will receive a personalized QRVN award and share a check for EUR 1 000.</p>
    <p>QRVN will select the best poster whose author(s) will receive a personalized QRVN award and share a check for EUR 1 000.</p>
  </div>

  <div class="section-tab" style="left:278px;top:232px">Professional Development Courses</div>
  <div class="back-text" style="left:286px;top:260px;width:242px">
    <p>In addition to abstracts for papers we call proposals from individuals interested in teaching educational professional development courses (4 hours) on the topics described in the Call for Papers. Proposal should be submitted to Lauren Vadeboncoeur, the Program Chair of the 5th QRVN, via email (firstname.lastname@mail-example.org) also by 28.2.2014.</p>
  </div>

  <div class="section-tab" style="left:278px;top:340px">Important Dates:</div>
  <ul class="back-text dates-list" style="left:286px;top:366px;width:242px">
    <li>Abstract submission: <b>28.2.2014</b></li>
    <li>Notification of acceptance: <b>18.4.2014</b></li>
    <li>Papers in the final form: <b>20.6.2014</b></li>
  </ul>

  <div class="welcome-band">We look forward to welcoming you to the fourth OKUW-LDZB<br>Electronics Module-Assembly Conference QRVN 2014 in Saarela!</div>

  <div class="city-photo" role="img" aria-label="Grey-toned view of waterfront buildings and a cathedral dome"></div>

  <div class="chairs">
    <div><div class="chair__name">Sanna Reinikainen-Holm</div><div class="chair__role">General Chair</div></div>
    <div><div class="chair__name">Jari Kettunen</div><div class="chair__role">Executive Chair</div></div>
    <div><div class="chair__name">Lauren Vadeboncoeur</div><div class="chair__role">Program Chair</div></div>
  </div>

  <footer class="partner-footer">
    <div class="partner"><span class="partner__dot"></span>OKUW</div>
    <div class="partner">LDZB</div>
    <div class="partner partner--small"><span class="partner__sq"></span>Birchmoor University</div>
    <div class="partner"><span class="partner__dot"></span>uTROF</div>
  </footer>
</section>

</body>
</html>
```